Oil and Gas Exploration and Production company needs a business card design

We need a business card design using our logo and colors in the logo. We want a mainstream design.

```html
<!DOCTYPE html>
<html lang="en">
<head>
<meta charset="utf-8">
<title>Tahua Energy – Business Card</title>
<link rel="stylesheet" href="https://fonts.googleapis.com/css2?family=Mulish:wght@400;600;800&display=swap">
<style>
  :root {
    --backdrop: #c9cdcd;
    --paper: #ffffff;
    --ink: #232323;
    --gold: #d39b22;
    --gold-deep: #b9861a;
    --card-back: #262524;
  }
  * { box-sizing: border-box; margin: 0; padding: 0; }
  html, body { width: 1200px; height: 900px; overflow: hidden; }
  body {
    background: var(--backdrop);
    font-family: "Mulish", sans-serif;
    display: flex;
    flex-direction: column;
    align-items: center;
    justify-content: center;
    gap: 60px;
  }
  .card {
    position: relative;
    width: 600px;
    height: 343px;
    border-bottom: 6px solid var(--gold);
  }
  .card--front { background: var(--paper); color: var(--ink); }
  .card--back { background: var(--card-back); display: flex; align-items: center; justify-content: center; }

  .brand { position: absolute; left: 48px; top: 46px; display: flex; align-items: center; gap: 12px; }
  .brand__dot { width: 34px; height: 34px; border-radius: 50%; background: var(--ink); }
  .brand__name { font-weight: 800; font-size: 40px; letter-spacing: -0.5px; color: var(--ink); }

  .divider { position: absolute; left: 48px; right: 48px; height: 1.5px; background: var(--gold); }
  .divider--top { top: 140px; }
  .divider--bottom { bottom: 36px; }

  .contacts { position: absolute; left: 48px; top: 166px; list-style: none; }
  .contacts li { display: flex; align-items: center; gap: 10px; font-size: 16px; line-height: 27px; color: var(--ink); }
  .contacts svg { width: 14px; height: 14px; flex: none; }

  .person { position: absolute; right: 48px; bottom: 52px; text-align: right; }
  .person__name { font-size: 26px; font-weight: 600; color: var(--gold); }
  .person__title { font-size: 15px; color: var(--ink); margin-top: 2px; }

  .back-brand { display: flex; align-items: center; gap: 14px; }
  .back-brand__dot { width: 40px; height: 40px; border-radius: 50%; background: var(--gold); }
  .back-brand__name { font-weight: 800; font-size: 38px; color: var(--gold); }
</style>
</head>
<body>
  <section class="card card--front">
    <div class="brand">
      <span class="brand__dot"></span>
      <span class="brand__name">Tahua Energy</span>
    </div>
    <div class="divider divider--top"></div>
    <ul class="contacts">
      <li>
        <svg viewBox="0 0 16 16" aria-hidden="true"><path fill="#d39b22" d="M3.6 1.5l2.3 2.6-1.3 1.8c.9 2 2.6 3.7 4.6 4.6l1.8-1.3 2.6 2.3-1.2 2.1C7.2 13.4 2.6 8.8 1.4 3.6z"/></svg>
        (555) 310-482-907
      </li>
      <li>
        <svg viewBox="0 0 16 16" aria-hidden="true"><rect x="1.5" y="3.5" width="13" height="9" fill="none" stroke="#d39b22" stroke-width="1.5"/><path d="M1.5 3.5L8 9l6.5-5.5" fill="none" stroke="#d39b22" stroke-width="1.5"/></svg>
        hello@tahua-energy.com
      </li>
      <li>
        <svg viewBox="0 0 16 16" aria-hidden="true"><g fill="none" stroke="#d39b22" stroke-width="1.3"><circle cx="8" cy="8" r="6.3"/><ellipse cx="8" cy="8" rx="2.8" ry="6.3"/><path d="M1.7 8h12.6M2.8 4.8h10.4M2.8 11.2h10.4"/></g></svg>
        www.tahua-energy.com
      </li>
    </ul>
    <div class="person">
      <div class="person__name">Daniel Reyes</div>
      <div class="person__title">CEO</div>
    </div>
    <div class="divider divider--bottom"></div>
  </section>

  <section class="card card--back">
    <div class="back-brand">
      <span class="back-brand__dot"></span>
      <span class="back-brand__name">Tahua Energy</span>
    </div>
  </section>
</body>
</html>
```